Corvane Partners Web Design

Dear all
I need a web design for a financial services site. We are a broker who deals with many different financial institutions and require a clean, simple and instantly impressive site based on the colour scheme that SketchGuild created for us. A landing page (www.crvnp.mx) gives an idea of the logo and clour scheme but we are looking at either a one page site with rollover text boxes or a 3 or 4 page site depending on the preference of the designer and the best user experience. The site“s purpose is to give confidence that the company exists rather than impart pages of information although we would like this to be a site that can expand over time as the company grows. For now the requirement is for a clear set of possibly changing images at the centre of a white screen that relate to finance in general nad the benefits of wealth creation as well as sectios either along the top or bottom - Our Company, Our Approach, Our services, Our clients, Contact (user to fill in contact box to be sent to info@crvnp.mx. The text for each of these boxes I assume can be added by the coding team here, it the overall look and feel that I am looking for from SketchGuild - deadline can be extended if necessary but I was hoping to wrap this all up in October

Target Market(s)

Succesful individuals looking to maximise returns on their investment via world class financial institutions and supported throughout by qualified independent financial advisors

Industry/Entity Type

Finance

Requirements
Must have
• Logo and color scheme of the logo design SketchGuild sent - I have all these sourcefiles, pantone and fonts

```html
<!DOCTYPE html>
<html lang="en">
<head>
<meta charset="utf-8">
<title>Corvane Partners — About &amp; Services</title>
<link rel="stylesheet" href="https://fonts.googleapis.com/css2?family=Jost:wght@200;300&family=Noto+Sans:wght@400&display=swap">
<style>
  :root {
    --page-bg: #ededed;
    --ink: #1f2d47;
    --navy: #1b3a60;
    --on-navy: #eef1f5;
    --icon-grey: #8a8a8a;
    --icon-light: #c9c9c9;
    --accent-orange: #f0a43a;
    --white: #ffffff;
  }
  * { margin: 0; padding: 0; box-sizing: border-box; }
  html, body {
    width: 1200px;
    height: 955px;
    overflow: hidden;
    background: var(--page-bg);
  }
  .page {
    position: relative;
    width: 1200px;
    height: 955px;
    color: var(--ink);
    font-family: "Noto Sans", Verdana, sans-serif;
  }
  .section-title {
    position: absolute;
    left: 0;
    width: 100%;
    text-align: center;
    font-family: "Jost", sans-serif;
    font-weight: 200;
    font-size: 42px;
    letter-spacing: 3px;
    line-height: 1;
    color: var(--ink);
  }
  .about-title { top: 72px; }
  .services-title { top: 350px; }
  .about-text {
    position: absolute;
    top: 163px;
    left: 0;
    width: 100%;
    text-align: center;
    font-size: 18.5px;
    letter-spacing: 0.5px;
    line-height: 33.3px;
  }
  .service {
    position: absolute;
    top: 436px;
    width: 351px;
    height: 445px;
    text-align: center;
  }
  .service--build { left: 73px; }
  .service--talk { left: 428px; background: var(--navy); color: var(--on-navy); overflow: hidden; }
  .service--grow { left: 800px; }
  .service-icon {
    display: block;
    margin: 48px auto 0;
    width: 54px;
    height: 54px;
  }
  .service-text {
    margin-top: 36px;
    font-size: 18.5px;
    letter-spacing: 0.5px;
    line-height: 33.2px;
  }
  .more-corner {
    position: absolute;
    right: 0;
    bottom: 0;
    width: 64px;
    height: 64px;
  }
</style>
</head>
<body>
<main class="page">
  <h2 class="section-title about-title">A LITTLE ABOUT US</h2>
  <p class="about-text">
    Lorem ipsum dolor sit amet, consectetuer adipiscing elit, sed diam nonummy nibh euismod tincidunt<br>
    ut laoreet dolore magna aliquam erat volutpat. Ut wisi enim ad minim veniam,<br>
    quis nostrud exerci tation ullamcorper suscipit lobortis nisl
  </p>

  <h2 class="section-title services-title">OUR SERVICES</h2>

  <section class="service service--build">
    <svg class="service-icon" viewBox="0 0 56 56" aria-hidden="true">
      <g fill="var(--icon-grey)" transform="translate(28 28)">
        <g id="tooth">
          <rect x="-4" y="-27" width="8" height="9" rx="1"/>
        </g>
        <use href="#tooth" transform="rotate(30)"/>
        <use href="#tooth" transform="rotate(60)"/>
        <use href="#tooth" transform="rotate(90)"/>
        <use href="#tooth" transform="rotate(120)"/>
        <use href="#tooth" transform="rotate(150)"/>
        <use href="#tooth" transform="rotate(180)"/>
        <use href="#tooth" transform="rotate(210)"/>
        <use href="#tooth" transform="rotate(240)"/>
        <use href="#tooth" transform="rotate(270)"/>
        <use href="#tooth" transform="rotate(300)"/>
        <use href="#tooth" transform="rotate(330)"/>
        <circle r="20"/>
        <circle r="9" fill="var(--white)"/>
        <circle r="5.5" fill="var(--icon-grey)"/>
      </g>
    </svg>
    <p class="service-text">
      Lorem ipsum dolor sit amet,<br>
      consectetuer adipiscing elit,<br>
      sed diam nonummy nibh eu-<br>
      ismod tincidunt<br>
      ut laoreet dolore magna<br>
      aliquam erat volutpat
    </p>
  </section>

  <section class="service service--talk">
    <svg class="service-icon" viewBox="0 0 56 56" aria-hidden="true">
      <path d="M20 14 H48 a6 6 0 0 1 6 6 V36 a6 6 0 0 1 -6 6 H44 V52 L34 42 H26 a6 6 0 0 1 -6 -6 Z" fill="var(--white)" stroke="var(--navy)" stroke-width="2.5"/>
      <path d="M8 4 H40 a6 6 0 0 1 6 6 V28 a6 6 0 0 1 -6 6 H22 L12 42 V34 H8 a6 6 0 0 1 -6 -6 V10 a6 6 0 0 1 6 -6 Z" fill="var(--white)" stroke="var(--navy)" stroke-width="2.5"/>
    </svg>
    <p class="service-text">
      Lorem ipsum dolor sit amet,<br>
      consectetuer adipiscing elit,<br>
      sed diam nonummy nibh eu-<br>
      ismod tincidunt<br>
      ut laoreet dolore magna ali-<br>
      quam erat volutpat
    </p>
    <svg class="more-corner" viewBox="0 0 64 64" aria-label="More">
      <polygon points="64,0 64,64 0,64" fill="var(--accent-orange)"/>
      <line x1="64" y1="0" x2="0" y2="64" stroke="var(--white)" stroke-width="6"/>
      <path d="M42 44 H56 M49 37 V51" stroke="var(--ink)" stroke-width="2"/>
    </svg>
  </section>

  <section class="service service--grow">
    <svg class="service-icon" viewBox="0 0 56 56" aria-hidden="true">
      <path d="M26 30 V6 A24 24 0 1 0 50 30 Z" fill="var(--icon-grey)"/>
      <path d="M31 25 V2 A23 23 0 0 1 54 25 Z" fill="var(--icon-light)"/>
    </svg>
    <p class="service-text">
      Lorem ipsum dolor sit amet,<br>
      consectetuer adipiscing elit,<br>
      sed diam nonummy nibh eu-<br>
      ismod tincidunt<br>
      ut laoreet dolore magna<br>
      aliquam erat volutpat
    </p>
  </section>
</main>
</body>
</html>
```